Anzeigengestaltung für Apotheke
Zielgruppe
Lindmoor-Apotheke
klassische Vor Ort Apotheke, Zielgruppe ältere Menschen und Gesundheitsbewusste Menschen, die ihren Cholesterinwert wissen wollen.
Aufgabenstellung
Keine Speziellen, außer, dass unser Logo in die Anzeige integriert werden soll. Anzeige in DIN A 6 Format und sollte folgenden Inhalt haben:
Irgend ein Teaser : (Gern auch mal im Internet gucken bei anderen Apotheken)
Cholesterin- Woche vom 24.-29. Oktober
Wir messen Ihren Cholesterol Wert inklusive HDL, LDL und Gesamtcholesterin
Anmeldung erbeten bei Frau Hesse: hesse@lindmoor-apotheke.example oder unter 0761 58 72 19

```html
<!DOCTYPE html>
<html lang="de">
<head>
<meta charset="utf-8">
<title>Cholesterin-Woche – Lindmoor-Apotheke</title>
<link rel="stylesheet" href="https://fonts.googleapis.com/css2?family=Carlito:wght@400;700&display=swap">
<style>
  :root {
    --brand-green: #2b6a1e;
    --band-green: #1bcf95;
    --alert-red: #f40000;
    --ink: #111111;
    --white: #ffffff;
    --slogan-tint: #fbe3e3;
  }
  html, body {
    margin: 0;
    padding: 0;
    width: 848px;
    height: 1200px;
    overflow: hidden;
    background: var(--white);
    font-family: "Carlito", "Calibri", sans-serif;
    color: var(--ink);
  }
  .ad {
    position: relative;
    width: 848px;
    height: 1200px;
    background: var(--white);
  }
  .brand {
    position: absolute;
    top: 48px;
    left: 0;
    width: 848px;
    display: flex;
    justify-content: center;
    align-items: center;
    gap: 14px;
  }
  .brand-mark {
    width: 92px;
    height: 92px;
    border-radius: 50%;
    background: var(--brand-green);
  }
  .brand-name {
    font-size: 31px;
    font-weight: 700;
    color: var(--brand-green);
    letter-spacing: 0.2px;
  }
  .slogan {
    position: absolute;
    top: 142px;
    left: 448px;
    width: 262px;
    height: 60px;
    background: var(--slogan-tint);
    border-radius: 6px;
  }
  .band {
    position: absolute;
    top: 242px;
    left: 0;
    width: 848px;
    height: 808px;
    background: var(--band-green);
  }
  .headline {
    position: absolute;
    top: 296px;
    left: 0;
    width: 848px;
    margin: 0;
    text-align: center;
    font-size: 58px;
    font-weight: 700;
    line-height: 1;
  }
  .date-box {
    position: absolute;
    top: 409px;
    left: 137px;
    width: 595px;
    height: 85px;
    background: var(--alert-red);
    color: var(--white);
    font-size: 48px;
    font-weight: 700;
    display: flex;
    align-items: center;
    justify-content: center;
  }
  .offer, .signup {
    position: absolute;
    left: 108px;
    margin: 0;
    font-size: 36px;
    line-height: 48px;
  }
  .offer { top: 570px; }
  .signup { top: 774px; }
  .offer strong { font-weight: 700; }
  .footer {
    position: absolute;
    top: 1078px;
    left: 0;
    width: 848px;
    text-align: center;
    font-size: 13px;
    line-height: 18px;
  }
  .footer .title { font-weight: 700; font-size: 13.5px; margin-bottom: 2px; }
  .footer .sep { color: var(--band-green); padding: 0 3px; }
  .footer .web { font-weight: 700; }
</style>
</head>
<body>
  <main class="ad">
    <header class="brand">
      <span class="brand-name">Lindmoor</span>
      <span class="brand-mark" aria-hidden="true"></span>
      <span class="brand-name">Apotheke</span>
    </header>
    <div class="slogan" role="img" aria-label="Handgeschriebener Slogan der Apotheke"></div>

    <section class="band">
    </section>

    <h1 class="headline">Cholesterin-Woche</h1>
    <div class="date-box">24. - 29. Oktober</div>

    <p class="offer">Wir messen Ihren Cholesterin Wert<br>inkl. <strong>HDL, LDL</strong> und <strong>Gesamtcholesterin</strong></p>

    <p class="signup">Anmeldung erbeten bei Frau Hesse<br>Tel. 0761/58 72 19 oder<br>per E-Mail hesse@lindmoor-apotheke.example</p>

    <footer class="footer">
      <div class="title">Lindmoor-Apotheke <span class="sep">|</span> Apothekerin Dr. Marlene Vogt-Brandt</div>
      <div>Lindenweg 12 <span class="sep">•</span> 79100 Talheim <span class="sep">|</span> Fon 07 61 - 58 72 19 <span class="sep">•</span> Fax 07 61 - 58 72 20</div>
      <div>info@lindmoor-apotheke.example <span class="sep">|</span> <span class="web">www.lindmoor-apotheke.example</span></div>
    </footer>
  </main>
</body>
</html>
```